Tidecrest NZ Brand, Revenue, Promotions & Events

I need an innovative business card that pops my brand. I like the colours against darker gradients and i'm not afraid to be bold.

I run my own Business, Brand, Event & Promotion company. I specialise in breathing life into businesses and adding atmosphere to promotions and events. I am concept based lady that likes to test the boundaries and create stand out campaigns that connect with the consumer.

I have 12 years business experience in a realm of interesting fields form 11 years in coordinating international music festivals & promotions, 6 years in radio with 8 radio awards including a NZ radio award for best sales team in NZ and was the national brand and sales manager for New Zealands 1st indoor entertainment mall. With 10 years of experience in advertising sales, I have an eye for creating revenue streams for businesses and thrive on implementing campaigns that compliment those streams.

I love sayings like "Do what you love, love what you do" and believe that you can achieve anything you want.

I have been fortunate in my career that my connections have carried me without needing to promote my business however it is important that I start to do so.

Target Market(s)

Decision makers 25 to 54

Contact Information for Business Card

Petra Ollingham
Director
p. 022 587 3091
e. petra@tidecrest.nz
www.tidecrest.nz

FB, IG and Linkedin logo

Font styles to use
Sans Serif

Colors

Designer to choose colors to be used in the design.

Requirements
Must have
• Petra Ollingham
• Director
• p. 022 587 3091
• e. petra@tidecrest.nz
• www.tidecrest.nz
• FB, IG and Linkedin logo
Nice to have
• I am looking for a business card with character, that leaves my presence with my customer and makes them remember my brand & optimistic personality when i walk out the door.

```html
<!DOCTYPE html>
<html lang="en">
<head>
<meta charset="utf-8">
<title>Tidecrest NZ – Business Card</title>
<link rel="stylesheet" href="https://fonts.googleapis.com/css2?family=Nunito+Sans:wght@400;600;700;800&display=swap">
<style>
  :root {
    --stage: #1e1e1e;
    --brand-blue: #29a8e0;
    --brand-blue-soft: #4bb8e8;
    --card-white: #ffffff;
    --card-shade: #f2f2f2;
    --ink: #222222;
    --muted: #9a9a9a;
  }
  * { box-sizing: border-box; margin: 0; padding: 0; }
  html, body {
    width: 1200px; height: 1021px; overflow: hidden;
    background: var(--stage);
    font-family: "Nunito Sans", Arial, sans-serif;
  }
  .stage {
    position: relative; width: 1200px; height: 1021px;
  }
  .card {
    position: absolute; left: 250px; width: 700px; height: 400px;
    border-radius: 2px;
    box-shadow: 0 10px 30px rgba(0,0,0,0.5);
    overflow: hidden;
  }
  /* Back side */
  .card-back {
    top: 80px;
    background: linear-gradient(135deg, var(--brand-blue) 0%, var(--brand-blue-soft) 100%);
    display: flex; flex-direction: column; align-items: center; justify-content: center;
    color: var(--card-white);
  }
  .card-back .wordmark {
    font-weight: 800; font-size: 58px; letter-spacing: 4px; text-transform: uppercase;
    display: flex; align-items: center; gap: 16px;
  }
  .wordmark .dot {
    width: 22px; height: 22px; border-radius: 50%; background: currentColor; display: inline-block;
  }
  .card-back .tagline {
    margin-top: 6px; font-size: 17px; font-weight: 400; letter-spacing: 1.5px;
  }
  /* Front side */
  .card-front {
    top: 540px;
    background: linear-gradient(170deg, var(--card-white) 55%, var(--card-shade) 100%);
    color: var(--ink);
  }
  .card-front .brand {
    position: absolute; left: 44px; top: 36px;
  }
  .card-front .wordmark {
    color: var(--brand-blue); font-weight: 800; font-size: 44px; letter-spacing: 3px;
    text-transform: uppercase; display: flex; align-items: center; gap: 12px; line-height: 1;
  }
  .card-front .wordmark .dot { width: 16px; height: 16px; }
  .card-front .tagline {
    margin-top: 6px; font-size: 14px; color: var(--muted); letter-spacing: 1.2px;
  }
  .name-tab {
    position: absolute; left: 0; top: 150px; width: 14px; height: 44px;
    background: var(--brand-blue); border-radius: 0 6px 6px 0;
  }
  .identity { position: absolute; left: 44px; top: 144px; }
  .identity .person {
    color: var(--brand-blue); font-weight: 700; font-size: 28px; line-height: 1.1;
  }
  .identity .role { font-size: 19px; color: var(--ink); }
  .contacts {
    position: absolute; left: 44px; top: 236px; list-style: none;
    font-size: 20px; line-height: 30px;
  }
  .contacts li { display: flex; align-items: center; gap: 10px; }
  .contacts svg { width: 17px; height: 17px; fill: none; stroke: var(--brand-blue); stroke-width: 2; }
  .contacts svg.solid { fill: var(--brand-blue); stroke: none; }
  .socials { position: absolute; left: 44px; top: 338px; display: flex; gap: 10px; }
  .socials span {
    width: 22px; height: 22px; border-radius: 4px; background: var(--brand-blue); display: block;
  }
</style>
</head>
<body>
<main class="stage">
  <section class="card card-back" role="img" aria-label="Blue card back with a repeating soft brand pattern behind the company name">
    <div class="wordmark"><span class="dot"></span>Tidecrest NZ</div>
    <div class="tagline">BRAND | REVENUE | EVENTS &amp; PROMOTIONS</div>
  </section>

  <section class="card card-front">
    <div class="brand">
      <div class="wordmark"><span class="dot"></span>Tidecrest NZ</div>
      <div class="tagline">BRAND | REVENUE | EVENTS &amp; PROMOTIONS</div>
    </div>

    <div class="name-tab"></div>
    <div class="identity">
      <div class="person">Petra Ollingham</div>
      <div class="role">Director</div>
    </div>

    <ul class="contacts">
      <li>
        <svg class="solid" viewBox="0 0 24 24"><path d="M6.6 10.8a15 15 0 0 0 6.6 6.6l2.2-2.2c.3-.3.7-.4 1-.2 1.1.4 2.3.6 3.6.6.6 0 1 .4 1 1V20c0 .6-.4 1-1 1C10.6 21 3 13.4 3 4c0-.6.4-1 1-1h3.5c.6 0 1 .4 1 1 0 1.3.2 2.5.6 3.6.1.3 0 .7-.2 1z"/></svg>
        022 587 3091
      </li>
      <li>
        <svg viewBox="0 0 24 24"><rect x="3" y="5" width="18" height="14" rx="1"/><path d="M3 6l9 7 9-7"/></svg>
        petra@tidecrest.nz
      </li>
      <li>
        <svg viewBox="0 0 24 24"><circle cx="12" cy="12" r="9"/><path d="M3 12h18M12 3c3 3 3 15 0 18M12 3c-3 3-3 15 0 18"/></svg>
        www.tidecrest.nz
      </li>
    </ul>

    <div class="socials" aria-label="Social media links">
      <span></span><span></span><span></span>
    </div>
  </section>
</main>
</body>
</html>
```